business card design for luxurious real estate brand

using the attached logo, i am looking for a 2-sided business card design. the back should be the gold logo on black background. the front needs to include: gold logo, name, phone, email, and website

Industry/Entity Type

real estate

Contact Information for Business Card

logo, name, email, phone, website

Font styles to use
Sans Serif

```html
<!DOCTYPE html>
<html lang="en">
<head>
<meta charset="utf-8">
<title>Casa Verano – Business Cards</title>
<link rel="stylesheet" href="https://fonts.googleapis.com/css2?family=Fira+Sans:wght@300;400;500;600&display=swap">
<style>
  :root {
    --backdrop: #7f9bbd;
    --card-black: #141414;
    --card-edge: #c9962a;
    --brand-yellow: #f9c80e;
    --text-white: #f4f4f4;
    --text-grey: #9a9a9a;
  }
  * { box-sizing: border-box; margin: 0; padding: 0; }
  html, body {
    width: 1200px; height: 876px; overflow: hidden;
    background: var(--backdrop);
    font-family: "Fira Sans", sans-serif;
  }
  .canvas {
    width: 1200px; height: 876px;
    display: flex; align-items: center; justify-content: center; gap: 80px;
  }
  .card {
    position: relative;
    width: 520px; height: 300px;
    background: radial-gradient(ellipse at 40% 30%, #232323 0%, var(--card-black) 70%);
    border-radius: 4px;
    box-shadow: 0 0 0 2px var(--card-edge), 0 18px 30px rgba(20, 35, 60, 0.35);
    overflow: hidden;
  }

  /* Front */
  .card-front .brand-mark {
    position: absolute; left: 34px; top: 40px;
    display: flex; align-items: center; gap: 12px;
  }
  .brand-square {
    width: 34px; height: 34px; background: var(--brand-yellow);
  }
  .brand-name {
    color: var(--brand-yellow);
    font-weight: 500; font-size: 22px; letter-spacing: 4px;
  }
  .contact-block {
    position: absolute; right: 34px; top: 40px;
    text-align: right;
  }
  .person-name {
    color: var(--text-white);
    font-size: 26px; font-weight: 500; letter-spacing: 4px;
  }
  .person-role {
    color: var(--text-grey);
    font-size: 13px; font-weight: 300; letter-spacing: 1px;
    margin-top: 6px;
  }
  .role-rule {
    width: 56px; height: 3px; background: var(--brand-yellow);
    margin: 8px 0 0 auto;
  }
  .contact-list { list-style: none; margin-top: 18px; }
  .contact-item {
    display: flex; justify-content: flex-end; align-items: flex-start; gap: 14px;
    color: var(--text-white);
    font-size: 14px; font-weight: 300; line-height: 1.35;
    margin-bottom: 6px;
  }
  .contact-icon { width: 16px; height: 16px; flex: none; margin-top: 2px; fill: var(--text-white); }
  .website {
    position: absolute; left: 34px; bottom: 28px;
    color: var(--text-white);
    font-size: 16px; font-weight: 500; letter-spacing: 2px;
  }

  /* Back */
  .card-back { display: flex; align-items: center; justify-content: center; }
  .card-back .brand-mark { display: flex; align-items: center; gap: 14px; }
  .card-back .brand-square { width: 40px; height: 40px; }
  .card-back .brand-name { font-size: 26px; letter-spacing: 6px; }
</style>
</head>
<body>
<main class="canvas">
  <section class="card card-front" aria-label="Business card front">
    <div class="brand-mark">
      <span class="brand-square"></span>
      <span class="brand-name">CASA VERANO</span>
    </div>
    <div class="contact-block">
      <h1 class="person-name">MARK ELLERY</h1>
      <p class="person-role">REALTOR</p>
      <div class="role-rule"></div>
      <ul class="contact-list">
        <li class="contact-item">
          <span>555-014-2290</span>
          <svg class="contact-icon" viewBox="0 0 16 16"><path d="M4 1h3l1 4-2 1a8 8 0 0 0 4 4l1-2 4 1v3c0 1-1 2-2 2A12 12 0 0 1 2 3c0-1 1-2 2-2z"/></svg>
        </li>
        <li class="contact-item">
          <span>hello@casaverano.com</span>
          <svg class="contact-icon" viewBox="0 0 16 16"><path d="M1 3h14v10H1z M2 4l6 5 6-5" fill="none" stroke="#f4f4f4" stroke-width="1.2"/></svg>
        </li>
        <li class="contact-item">
          <span>118 Orchard Lane, Fairview<br>California - 95000</span>
          <svg class="contact-icon" viewBox="0 0 16 16"><path d="M8 1a5 5 0 0 0-5 5c0 4 5 9 5 9s5-5 5-9a5 5 0 0 0-5-5zm0 7a2 2 0 1 1 0-4 2 2 0 0 1 0 4z"/></svg>
        </li>
      </ul>
    </div>
    <p class="website">WWW.CASAVERANO.COM</p>
  </section>

  <section class="card card-back" aria-label="Business card back">
    <div class="brand-mark">
      <span class="brand-square"></span>
      <span class="brand-name">CASA VERANO</span>
    </div>
  </section>
</main>
</body>
</html>
```